Need a Modern WIX Website design

Need help designing a modern WIX website. I already started building on studio.plovex.com but I am not a designer and would like a more modern, update aesthetic look. This is not an e-commerce site. Just a website portraying our company, posting what products we offer, contact, about us, services. Logo is already on the studio.plovex version with some content. Need a designer with vision, and ingenuity to set it apart change it a little and make it stand out. Please look at the current site for redesign and/or ideas https://norvatradeco.plovexsite.com/website
also need the design to be connected to our google domain www.nvt.trade

Please feel free to ask as many questions as possible

Target Market(s)

Tire repair shops, Tire stores, mechanic shops, tire replacement franchises, wheel and rim stores

Industry/Entity Type

we are wholesalers, B2B ..sell tire repair materials, tire hand tools, machinery, chemicals, wheel lug nuts, wheel accessories

Coding

Coded - Design and coding required

Number of Pages Required

5+ page

Font styles to use
Other font styles liked:
• Let designer choose

Colors

Designer to choose colors to be used in the design.

Requirements
Must have
• modern design layout, videos, high quality pictures, different ideas for pages (Home, shop, about, products, services, contact, faq, meet the team) translatable english to spanish
Nice to have
• would like to have an up to date modern look, interactive, easy to navigate,
Should not have
• not be hard to navigate for our customers

```html
<!DOCTYPE html>
<html lang="en">
<head>
<meta charset="utf-8">
<title>Norva Trade Co. — Services</title>
<link rel="stylesheet" href="https://fonts.googleapis.com/css2?family=Barlow:wght@400;500;600&family=Rajdhani:wght@600;700&family=Michroma&display=swap">
<style>
:root{
  --red:#e2232a;
  --black:#000;
  --ink:#111;
  --panel:#1c1c1c;
  --bar:#2d2d2d;
  --nav:#1e1e1e;
  --frame:#3a3a3a;
  --grey:#8a8a8a;
  --white:#fff;
  --muted:#d6d6d6;
}
*{margin:0;padding:0;box-sizing:border-box}
html,body{width:1200px;height:3659px;overflow:hidden;background:var(--black)}
body{position:relative;font-family:'Barlow',sans-serif;color:var(--white)}
.abs{position:absolute}
.head{font-family:'Rajdhani',sans-serif;font-weight:700;text-transform:uppercase;letter-spacing:.3px}
.rule{position:absolute;height:3px;background:var(--red)}

/* top bar */
.topbar{left:0;top:0;width:1200px;height:31px;background:var(--bar);font-size:10px;color:var(--muted)}
.topbar .item{position:absolute;top:9px;display:flex;align-items:center;gap:6px}
.topbar .search{position:absolute;left:634px;top:2px;width:222px;height:27px;background:var(--white);color:#222;font-size:12px;font-weight:600;padding:6px 14px}
.topbar .links{position:absolute;top:9px;font-size:12px}
.topbar .slash{position:absolute;left:1014px;top:4px;width:1px;height:26px;background:#999;transform:rotate(20deg)}

/* nav */
.nav{left:0;top:31px;width:1200px;height:90px;background:var(--nav)}
.brand{position:absolute;display:flex;align-items:center;gap:10px;font-family:'Rajdhani',sans-serif;font-weight:700;color:var(--white);text-transform:uppercase}
.brand .mark{border:2px solid var(--red);width:34px;height:34px}
.nav .menu{position:absolute;top:40px;font-size:13px;font-weight:600;letter-spacing:.3px}
.nav .menu.active::after{content:"";position:absolute;left:0;right:0;top:22px;height:2px;background:var(--red)}
.call{left:1004px;top:31px;width:196px;height:90px;background:var(--red)}
.call .label{position:absolute;left:56px;top:26px;font-size:13px}
.call .num{position:absolute;left:56px;top:42px;font-size:19px;font-weight:600}

/* hero */
.hero{left:0;top:121px;width:1200px;height:376px;background:linear-gradient(100deg,#1a1a1a 0%,#2b2622 40%,#5a5550 70%,#242424 100%)}
.hero .kicker{position:absolute;left:115px;top:142px;font-family:'Michroma',sans-serif;font-size:16px;letter-spacing:2px}
.hero .title{position:absolute;left:113px;top:166px;font-family:'Michroma',sans-serif;font-size:36px;letter-spacing:2px}

/* feature cards */
.section-title{font-family:'Rajdhani',sans-serif;font-weight:700;font-size:38px;text-align:center;width:1200px;left:0}
.frame{border:4px solid var(--frame)}
.photo{background:linear-gradient(135deg,#2f3946,#5d6266 55%,#1b1b1b)}
.redframe{background:var(--red)}
.greyframe{background:var(--grey)}
.card-title{font-size:27px}
.card-body{font-size:14.5px;line-height:24px;color:var(--muted);width:390px}

/* why */
.why{left:0;top:2471px;width:1200px;height:821px;background:var(--ink)}
.bubble{position:absolute;width:102px;height:102px;border-radius:50%;border:3px solid var(--red);background:radial-gradient(circle,#6a6a6a,#2a2a2a)}
.trait h3{font-family:'Rajdhani',sans-serif;font-weight:700;font-size:20px;letter-spacing:.5px}
.trait p{font-size:11.5px;line-height:18px;color:var(--muted);margin-top:3px}

/* footer */
.footer{left:0;top:3292px;width:1200px;height:367px;background:#141414}
.footer h4{font-family:'Rajdhani',sans-serif;font-weight:700;font-size:18px}
.footer .fl{font-size:11.5px;color:var(--muted);line-height:23.4px}
.field{position:absolute;left:848px;width:197px;background:var(--white);color:#555;font-size:9px;padding:5px 12px}
.social{position:absolute;top:3460px;width:27px;height:27px;border:2px solid var(--red)}
</style>
</head>
<body>

<!-- top bar -->
<div class="abs topbar">
  <div class="item" style="left:106px">
    <svg width="14" height="14" viewBox="0 0 14 14"><circle cx="7" cy="7" r="7" fill="#9a9a9a"/><path d="M7 3a2.6 2.6 0 0 0-2.6 2.6C4.4 8 7 11 7 11s2.6-3 2.6-5.4A2.6 2.6 0 0 0 7 3z" fill="#2d2d2d"/></svg>
    218 Harbor Mill Road Oakview, CA 90210
  </div>
  <div class="item" style="left:378px">
    <svg width="14" height="14" viewBox="0 0 14 14"><circle cx="7" cy="7" r="7" fill="#9a9a9a"/><rect x="3.5" y="4.5" width="7" height="5" fill="#2d2d2d"/></svg>
    norvatradeco@mailbox.com
  </div>
  <div class="search">Search Product
    <svg class="abs" style="right:10px;top:8px" width="11" height="11" viewBox="0 0 11 11"><circle cx="4.5" cy="4.5" r="3.3" fill="none" stroke="#e2232a" stroke-width="1.6"/><path d="M7 7l3 3" stroke="#e2232a" stroke-width="1.6"/></svg>
  </div>
  <div class="links" style="left:976px">FAQ</div>
  <div class="slash"></div>
  <div class="links" style="left:1041px">CONTACT</div>
</div>

<!-- nav -->
<div class="abs nav">
  <div class="brand" style="left:101px;top:26px;font-size:24px"><span class="mark"></span>Norva Trade Co.</div>
  <div class="menu active" style="left:363px">SHOP</div>
  <div class="menu" style="left:430px">ABOUT</div>
  <div class="menu" style="left:504px">PRODUCTS</div>
  <div class="menu" style="left:602px">SERVICES</div>
  <div class="menu" style="left:694px">MEET THE TEAM</div>
  <div class="menu" style="left:823px">WHEEL LUG NUTS &amp; BOLTS</div>
</div>
<div class="abs call">
  <svg class="abs" style="left:16px;top:28px" width="32" height="32" viewBox="0 0 32 32"><circle cx="16" cy="16" r="16" fill="#fff"/><path d="M11 9l3 0 1.5 4-2 1.5a10 10 0 0 0 4 4l1.5-2 4 1.5v3c0 1-1 2-2 2A13 13 0 0 1 9 11c0-1 1-2 2-2z" fill="#e2232a"/></svg>
  <div class="label">CALL US TODAY</div>
  <div class="num">800-555-0142</div>
</div>

<!-- hero -->
<div class="abs hero" role="img" aria-label="Mechanic tightening the lug nuts of a car wheel with an impact wrench">
  <div class="kicker">SERVICES PROVIDE</div>
  <div class="title">WHAT WE DO</div>
</div>

<!-- services offered -->
<div class="abs section-title" style="top:561px">SERVICES OFFERED</div>
<div class="rule" style="left:567px;top:609px;width:66px"></div>

<!-- card 1 -->
<div class="abs frame" style="left:122px;top:680px;width:653px;height:446px"></div>
<div class="abs greyframe" style="left:916px;top:694px;width:176px;height:138px"></div>
<div class="abs redframe" style="left:608px;top:784px;width:350px;height:292px"></div>
<div class="abs photo" style="left:618px;top:706px;width:461px;height:359px" role="img" aria-label="Gloved hands checking the tread of a tyre"></div>
<div class="abs head card-title" style="left:169px;top:752px">STELLAR CUSTOMER SERVICE</div>
<div class="rule" style="left:169px;top:792px;width:64px;height:2px"></div>
<p class="abs card-body" style="left:169px;top:817px">For over 25 years, we have been providing excellent customer service by going the extra mile in making sure a customer is happy and satisfied with our company's products or services. We take pride in providing service to a customer in a timely, pleasant manner. In our continuous goal to provide excellent customer service, we have incorporated superb communication and problem resolution skills.</p>

<!-- card 2 -->
<div class="abs" style="left:0;top:1204px;width:1200px;height:621px;background:var(--panel)"></div>
<div class="abs frame" style="left:454px;top:1291px;width:654px;height:446px"></div>
<div class="abs greyframe" style="left:94px;top:1321px;width:190px;height:137px"></div>
<div class="abs redframe" style="left:236px;top:1406px;width:377px;height:291px"></div>
<div class="abs photo" style="left:102px;top:1329px;width:497px;height:357px;background:linear-gradient(160deg,#2a2a2a,#0e0e0e 60%,#3a3a3a)" role="img" aria-label="Stack of new tyres in low light"></div>
<div class="abs head card-title" style="left:669px;top:1426px">HIGH QUALITY PRODUCTS</div>
<div class="rule" style="left:669px;top:1465px;width:64px;height:2px"></div>
<p class="abs card-body" style="left:669px;top:1483px;width:400px">Our products are trusted for their design &amp; engineering, &amp; we will continue to equip our customers with high-quality products and tools at the best value</p>

<!-- card 3 -->
<div class="abs frame" style="left:114px;top:1893px;width:653px;height:446px"></div>
<div class="abs greyframe" style="left:909px;top:1910px;width:174px;height:136px"></div>
<div class="abs redframe" style="left:599px;top:1998px;width:350px;height:291px"></div>
<div class="abs photo" style="left:609px;top:1920px;width:460px;height:358px" role="img" aria-label="Mechanic in a work jacket fitting a wheel in a garage"></div>
<div class="abs head card-title" style="left:172px;top:1982px">COMMITMENT</div>
<div class="rule" style="left:172px;top:2021px;width:64px;height:2px"></div>
<p class="abs card-body" style="left:172px;top:2046px">When a customer comes to us for parts it is often in the context of a long project. We offer Tire Alignment services that will help guide you throughout the course of your automobile restoration and will save you time and money. This is what differentiates us from other vehicle part replacement stores. Come in and see what we've got to offer you.</p>

<!-- why choose us -->
<div class="abs why"></div>
<div class="abs" style="left:0;top:2545px;width:1200px;text-align:center;font-family:'Michroma',sans-serif;font-size:13px;letter-spacing:2px;color:var(--muted)">WHY WE ARE</div>
<div class="abs section-title" style="top:2565px">WHY CHOOSE US</div>
<div class="rule" style="left:567px;top:2609px;width:66px"></div>

<div class="abs" style="left:398px;top:2648px;width:412px;height:412px;border-radius:50%;border:2px solid #3a3a3a;background:radial-gradient(circle,#3a3a3a,#151515 75%)" role="img" aria-label="Dark background of stacked tyres"></div>
<div class="abs" style="left:521px;top:2771px;width:166px;height:166px;border:6px solid var(--white)"></div>
<div class="abs head" style="left:521px;top:2831px;width:166px;text-align:center;font-size:40px">NVT</div>

<div class="bubble" style="left:408px;top:2665px" role="img" aria-label="Mechanic at work"></div>
<div class="bubble" style="left:704px;top:2668px" role="img" aria-label="Smiling tyre technician"></div>
<div class="bubble" style="left:355px;top:2888px" role="img" aria-label="Tyre tread close-up"></div>
<div class="bubble" style="left:724px;top:2887px" role="img" aria-label="Handshake"></div>
<div class="bubble" style="left:544px;top:3009px" role="img" aria-label="Hand holding a five star rating"></div>

<div class="abs trait" style="left:150px;top:2678px;width:246px;text-align:right">
  <h3>INNOVATION</h3>
  <p>We keep innovating to improve the experience for customers and everyone who uses our spaces.</p>
</div>
<div class="abs trait" style="left:819px;top:2673px;width:262px">
  <h3>SIMPLICITY</h3>
  <p>We get things done simply and flexibly. We remove unnecessary obstacles so that we are focused on our customers to deal with.</p>
</div>
<div class="abs trait" style="left:92px;top:2919px;width:255px;text-align:right">
  <h3>PROACTIVITY</h3>
  <p>We resolve problems as quick as possible and can be trusted to do as we say.</p>
</div>
<div class="abs trait" style="left:839px;top:2906px;width:245px">
  <h3>COMMITMENT</h3>
  <p>We understand, respect and value our customers, taking an interest and the time to listen.</p>
</div>
<div class="abs trait" style="left:389px;top:3126px;width:400px;text-align:center">
  <h3>EXCELLENCE</h3>
  <p>We achieve high quality in everything we do, committing to excellence in how we do business.</p>
</div>

<!-- footer -->
<div class="abs footer"></div>
<div class="brand" style="left:136px;top:3366px;font-size:22px"><span class="mark" style="width:30px;height:30px"></span>Norva Trade Co.</div>
<div class="social" style="left:141px" aria-label="Social link"></div>
<div class="social" style="left:192px" aria-label="Social link"></div>
<div class="social" style="left:241px" aria-label="Social link"></div>

<h4 class="abs" style="left:421px;top:3348px;position:absolute">QUICK LINKS</h4>
<div class="abs" style="left:421px;top:3377px;width:146px;height:1px;background:#3a3a3a"></div>
<div class="abs" style="left:421px;top:3377px;width:26px;height:1px;background:var(--white)"></div>
<div class="abs fl" style="left:423px;top:3386px">Shop<br>FAQ<br>Meet the Team<br>Wheel Lug Nuts &amp; Bolts<br>About<br>Products<br>Services</div>

<h4 class="abs" style="left:616px;top:3348px;position:absolute">CONTACT US</h4>
<div class="abs" style="left:616px;top:3377px;width:146px;height:1px;background:#3a3a3a"></div>
<div class="abs" style="left:616px;top:3377px;width:26px;height:1px;background:var(--white)"></div>
<svg class="abs" style="left:620px;top:3396px" width="16" height="16" viewBox="0 0 14 14"><circle cx="7" cy="7" r="7" fill="#9a9a9a"/><path d="M7 3a2.6 2.6 0 0 0-2.6 2.6C4.4 8 7 11 7 11s2.6-3 2.6-5.4A2.6 2.6 0 0 0 7 3z" fill="#141414"/></svg>
<div class="abs fl" style="left:644px;top:3390px;line-height:15px">218 Harbor Mill Road<br>Oakview, CA 90210</div>
<svg class="abs" style="left:620px;top:3441px" width="16" height="16" viewBox="0 0 14 14"><circle cx="7" cy="7" r="7" fill="#9a9a9a"/><path d="M4.5 3.5h2l.8 2-1 .8a5 5 0 0 0 2 2l.8-1 2 .8v2c0 .5-.5 1-1 1A7 7 0 0 1 3.5 4.5c0-.5.5-1 1-1z" fill="#141414"/></svg>
<div class="abs fl" style="left:644px;top:3437px">Toll Free <b style="color:#fff">800-555-0142</b></div>
<svg class="abs" style="left:620px;top:3473px" width="16" height="16" viewBox="0 0 14 14"><circle cx="7" cy="7" r="7" fill="#9a9a9a"/><rect x="3.5" y="4.5" width="7" height="5" fill="#141414"/></svg>
<div class="abs fl" style="left:644px;top:3469px">norvatradeco@mailbox.com</div>

<h4 class="abs" style="left:846px;top:3348px;position:absolute">GET A QUOTE NOW</h4>
<div class="abs" style="left:846px;top:3377px;width:26px;height:1px;background:var(--white)"></div>
<div class="field" style="top:3395px;height:21px">Name</div>
<div class="field" style="top:3424px;height:21px">Email address</div>
<div class="field" style="top:3453px;height:21px">Phone</div>
<div class="field" style="top:3482px;height:45px">Message</div>
<div class="abs" style="left:849px;top:3536px;width:199px;height:27px;background:var(--red);font-size:10px;font-weight:600;text-align:center;line-height:27px">SEND MESSAGE</div>

<div class="abs" style="left:0;top:3607px;width:1200px;height:1px;background:#2e2e2e"></div>
<div class="abs" style="left:0;top:3630px;width:1200px;text-align:center;font-size:10.5px;color:var(--muted)">©2022 by Norva Trade Co. Inc.</div>

</body>
</html>
```